Label design for Japanese sake bottle (American market targeted)

We are launching a new sake product and the product concept is as below.

1. It is a draft which means it has a fresh taste
2. We want to emphasize on its cleanness and that it's easy drinkable
3. It is most likely to have a light blue transparent 300ml bottle
4. Product name is "Brisk Harbor Pour" although you don't have to make them stand out on the label. We are targeting non-Japanese customers, so all we want them to know is that "it is a sake and easy drinkable"
5. It is affordable. Its retail price per bottle would be somewhere around $10

Target Market(s)

Non-Japanese, preferably non-Asian liquor / grocery stores and restaurants

Industry/Entity Type

Glass Bottle

Font styles to use
Serif
Sans Serif
Decorative

Colors

Designer to choose colors to be used in the design.

Requirements
Must have
• The word "sake"
• Pureness, cleanness
Nice to have
• Any ideas for entering non-Asian market will be welcome!
Should not have
• Please do NOT make it similar to our competitors (which I would attach a few images of)

```html
<!DOCTYPE html>
<html lang="en">
<head>
<meta charset="utf-8">
<title>Brisk Harbor Pour – Sake Label</title>
<link href="https://fonts.googleapis.com/css2?family=Share+Tech+Mono&display=swap" rel="stylesheet">
<style>
  :root {
    --paper: #ffffff;
    --sun: #f7b343;
    --ink-navy: #2e3192;
    --sea-deep: #a9a8d6;
    --sea-mid: #cfcfe6;
    --sea-pale: #f1f1f7;
    --label-orange: #f6b040;
  }
  html, body {
    margin: 0;
    padding: 0;
    overflow: hidden;
    background: var(--paper);
  }
  .label {
    position: relative;
    width: 834px;
    height: 1200px;
    overflow: hidden;
    background: var(--paper);
  }
  .label__art {
    position: absolute;
    inset: 0;
    width: 834px;
    height: 1200px;
  }
  .label__category {
    font-family: "Share Tech Mono", monospace;
    font-weight: 400;
    font-size: 220px;
    fill: var(--ink-navy);
  }
  .label__product {
    position: absolute;
    left: 0;
    right: 0;
    top: 1092px;
    margin: 0;
    text-align: center;
    font-family: "Share Tech Mono", monospace;
    font-weight: 400;
    font-size: 40px;
    line-height: 1;
    font-variant: small-caps;
    letter-spacing: 0.28em;
    word-spacing: 0.1em;
    color: var(--label-orange);
    padding-left: 0.28em;
    white-space: nowrap;
  }
</style>
</head>
<body>
  <main class="label">
    <svg class="label__art" viewBox="0 0 834 1200" xmlns="http://www.w3.org/2000/svg">
      <defs>
        <linearGradient id="seaWash" x1="0" y1="0" x2="0" y2="1">
          <stop offset="0" stop-color="var(--sea-deep)"/>
          <stop offset="0.35" stop-color="var(--sea-mid)"/>
          <stop offset="1" stop-color="var(--sea-pale)"/>
        </linearGradient>
      </defs>

      <path class="sun" d="M136 368 A296 296 0 0 1 728 368 Z" fill="var(--sun)"/>

      <text class="label__category" x="426" y="318" text-anchor="middle">saké</text>

      <path class="sea-wash" role="img" aria-label="Watercolour sea with splashes and sun reflection, fading to white"
            d="M8 364 L834 364 L834 930 Q800 990 740 992 L420 980 Q200 940 16 812 L10 600 Z"
            fill="url(#seaWash)"/>
    </svg>

    <p class="label__product">Brisk Harbor Pour</p>
  </main>
</body>
</html>
```